Business Card

Yes I would like you to design me a business card with the logo you just made me

Industry/Entity Type

Business

Colors
33b7a4
00a990
333333
000000
757575
7f7f7f

```html
<!DOCTYPE html>
<html lang="en">
<head>
<meta charset="utf-8">
<title>Marina Velasco Photography – Business Card</title>
<link rel="stylesheet" href="https://fonts.googleapis.com/css2?family=Arimo:wght@400&family=Allura&display=swap">
<style>
  :root {
    --backdrop: #333333;
    --front-green: #00a990;
    --front-green-light: #33b7a4;
    --back-blue: #38a3d8;
    --back-blue-dark: #2f95c9;
    --band-green: #00a990;
    --ink-white: #ffffff;
    --edge-shadow: rgba(0, 0, 0, 0.45);
  }
  * { box-sizing: border-box; margin: 0; padding: 0; }
  html, body {
    width: 1200px; height: 1000px; overflow: hidden;
    background: var(--backdrop);
  }
  .canvas {
    position: relative; width: 1200px; height: 1000px;
    display: flex; flex-direction: column; align-items: center; justify-content: center; gap: 60px;
  }
  .card {
    position: relative; width: 700px; height: 400px; overflow: hidden;
    color: var(--ink-white);
    box-shadow: 0 10px 30px var(--edge-shadow);
  }
  /* Front face */
  .card--front {
    background: radial-gradient(ellipse at 40% 35%, var(--front-green-light) 0%, var(--front-green) 65%, #00957f 100%);
    display: flex; flex-direction: column; align-items: center; justify-content: center; gap: 26px;
  }
  .front-mark {
    width: 120px; height: 120px; border-radius: 50%;
    background: var(--ink-white);
  }
  .front-name {
    font-family: "Arimo", sans-serif; font-weight: 400;
    font-size: 64px; letter-spacing: 1px; line-height: 1;
  }
  .front-tagline {
    font-family: "Arimo", sans-serif; font-weight: 400;
    font-size: 22px; letter-spacing: 12px; margin-top: -10px;
  }
  /* Back face */
  .card--back {
    background: radial-gradient(ellipse at 60% 60%, var(--back-blue) 0%, var(--back-blue) 55%, var(--back-blue-dark) 100%);
  }
  .title-band {
    position: absolute; left: 0; right: 0; top: 34px; height: 72px;
    background: var(--band-green);
    display: flex; align-items: center; justify-content: center; gap: 14px;
  }
  .title-band__name { font-family: "Allura", cursive; font-size: 44px; }
  .title-band__divider { font-family: "Arimo", sans-serif; font-size: 32px; }
  .title-band__role { font-family: "Arimo", sans-serif; font-size: 32px; letter-spacing: 0.5px; }

  .brand {
    position: absolute; top: 128px; left: 0; right: 0;
    display: flex; flex-direction: column; align-items: center;
  }
  .brand__mark {
    width: 40px; height: 40px; border-radius: 50%; background: var(--ink-white);
  }
  .brand__name {
    font-family: "Arimo", sans-serif; font-weight: 400; font-size: 30px; margin-top: 8px; line-height: 1;
  }
  .brand__tagline {
    font-family: "Arimo", sans-serif; font-weight: 400; font-size: 11px; letter-spacing: 5px; margin-top: 4px;
  }
  .contact {
    position: absolute; top: 262px; left: 0; right: 0;
    text-align: center; font-family: "Arimo", sans-serif; font-size: 19px; line-height: 30px;
  }
  .contact__label { font-family: "Allura", cursive; font-size: 26px; margin-right: 4px; }
  .contact__sep { margin: 0 10px; }
  .location {
    position: absolute; bottom: 18px; left: 0; right: 0; text-align: center;
    font-family: "Allura", cursive; font-size: 30px;
  }
</style>
</head>
<body>
<main class="canvas">
  <section class="card card--front" aria-label="Card front">
    <div class="front-mark"></div>
    <div class="front-name">marina velasco</div>
    <div class="front-tagline">PHOTOGRAPHY</div>
  </section>

  <section class="card card--back" aria-label="Card back">
    <div class="title-band">
      <span class="title-band__name">marina velasco</span>
      <span class="title-band__divider">|</span>
      <span class="title-band__role">photographer</span>
    </div>
    <div class="brand">
      <div class="brand__mark"></div>
      <div class="brand__name">marina velasco</div>
      <div class="brand__tagline">PHOTOGRAPHY</div>
    </div>
    <div class="contact">
      <p><span class="contact__label">cell</span> 555-012.4478<span class="contact__sep">|</span><span class="contact__label">email</span> marinavelascophoto@example.com</p>
      <p>marinavelasco.example/photography</p>
    </div>
    <div class="location">Fairhaven Ma</div>
  </section>
</main>
</body>
</html>
```